Business card for new consulting business - Brackenvale Enterprises Pty Ltd.

Consulting in the areas of Occupational Health, Safety and Community Relations in the resources (mining) industries. The consultant (me) will work both within Australia and overseas jurisdictions such as South East Asia, Africa , South America etc, often working with third world indigenous communities. The design should suggest a high level of social and environmental responsibility.

```html
<!DOCTYPE html>
<html lang="en">
<head>
<meta charset="utf-8">
<title>Brackenvale Enterprises Pty Ltd – Business Card</title>
<link rel="stylesheet" href="https://fonts.googleapis.com/css2?family=Lato:wght@400;700&family=Ubuntu:wght@500;700&display=swap">
<style>
  :root {
    --backdrop: #161616;
    --card: #232323;
    --card-edge: #2c2c2c;
    --brand-blue: #1a7fd1;
    --ink-light: #f2f2f2;
    --ink-muted: #d9d9d9;
  }
  * { margin: 0; padding: 0; box-sizing: border-box; }
  html, body {
    width: 1200px;
    height: 900px;
    overflow: hidden;
    background: var(--backdrop);
  }
  .canvas {
    width: 1200px;
    height: 900px;
    display: flex;
    flex-direction: column;
    align-items: center;
    justify-content: center;
    gap: 28px;
  }
  .card {
    width: 700px;
    height: 400px;
    background: linear-gradient(135deg, var(--card) 0%, var(--card-edge) 100%);
    box-shadow: 0 12px 30px rgba(0,0,0,0.6);
    position: relative;
    display: flex;
    align-items: center;
  }

  /* brand name lockup */
  .brand {
    display: flex;
    align-items: center;
    gap: 14px;
    font-family: "Ubuntu", sans-serif;
    font-weight: 700;
    color: var(--brand-blue);
    line-height: 1.05;
  }
  .brand-square {
    flex: none;
    background: var(--brand-blue);
  }

  /* front */
  .card-front { justify-content: center; }
  .card-front .brand { font-size: 40px; }
  .card-front .brand-square { width: 62px; height: 62px; }

  /* back */
  .card-back { padding: 0 0 0 56px; }
  .card-back .brand { font-size: 25px; width: 260px; }
  .card-back .brand-square { width: 44px; height: 44px; }
  .divider {
    width: 2px;
    height: 210px;
    background: var(--brand-blue);
    margin: 0 38px 0 16px;
  }
  .contact {
    font-family: "Lato", sans-serif;
    color: var(--ink-light);
  }
  .contact-name {
    font-family: "Ubuntu", sans-serif;
    font-weight: 700;
    font-size: 32px;
    color: var(--brand-blue);
    line-height: 1;
  }
  .contact-role {
    font-size: 18px;
    margin: 4px 0 22px;
  }
  .contact-address {
    font-size: 18px;
    line-height: 1.3;
    margin-bottom: 16px;
  }
  .contact-list { list-style: none; }
  .contact-list li {
    display: flex;
    align-items: center;
    gap: 12px;
    font-size: 18px;
    line-height: 1.5;
  }
  .contact-list svg {
    width: 14px;
    height: 14px;
    flex: none;
    fill: none;
    stroke: var(--brand-blue);
    stroke-width: 1.6;
  }
  .web-domain { color: var(--brand-blue); }
</style>
</head>
<body>
<main class="canvas">

  <section class="card card-front" aria-label="Card front">
    <div class="brand">
      <span class="brand-square" aria-hidden="true"></span>
      <span class="brand-name">Brackenvale<br>Enterprises Pty Ltd</span>
    </div>
  </section>

  <section class="card card-back" aria-label="Card back">
    <div class="brand">
      <span class="brand-square" aria-hidden="true"></span>
      <span class="brand-name">Brackenvale<br>Enterprises Pty Ltd</span>
    </div>

    <div class="divider" aria-hidden="true"></div>

    <div class="contact">
      <h1 class="contact-name">Dana Whitfield</h1>
      <p class="contact-role">Founder</p>
      <p class="contact-address">480 Harbour View Rd.<br>Coral Springs, FL 33071</p>
      <ul class="contact-list">
        <li>
          <svg viewBox="0 0 16 16" aria-hidden="true"><path d="M4 1.5 L6.5 4.5 L5 6.5 Q6.5 9.5 9.5 11 L11.5 9.5 L14.5 12 L12.5 14.5 Q6 14 1.5 4 Z"/></svg>
          954-555-0147
        </li>
        <li>
          <svg viewBox="0 0 16 16" aria-hidden="true"><rect x="1.5" y="3.5" width="13" height="9"/><path d="M1.5 3.5 L8 9 L14.5 3.5"/></svg>
          info@brackenvaleenterprises.com
        </li>
        <li>
          <svg viewBox="0 0 16 16" aria-hidden="true"><circle cx="8" cy="8" r="6.5"/><ellipse cx="8" cy="8" rx="3" ry="6.5"/><path d="M1.5 8 H14.5 M2.5 4.8 H13.5 M2.5 11.2 H13.5"/></svg>
          <span>www.<span class="web-domain">brackenvaleenterprises</span>.com</span>
        </li>
      </ul>
    </div>
  </section>

</main>
</body>
</html>
```